velmorino.eu :: Design ideas (no coding) for key pages of Personalized greeting cards online store

We need your vision on modern, clean, easy to read user interface (UI) for online service of personalized printed products, like greeting cards, postcards, fridge magnets, clips and etc.
Your vision should include UI presentation for:
- Home page with login (including soc nets)
- Product Designer page
- Cart pages (products and address selection)
- Example of general internal page (pricing, terms, etc)
- Artist info and portfolio page
We are looking for ideas we will love, NOT complete design of a whole site.
Top design/vision will we used as a basement for separate contract on complete design of the site.

UI should be based on existing functionality with some extent. It should not break ideas or methods used on prototype but designers are free to offer own product presentations, designer’s layout and cart views.

Prototype:
English: http://velmorino.eu
Russian: http://velmorino.ru
Lithuanian: http://velmorino.lt

Target Market(s)

People of 16-45 y.o. who likes to be distinctive, personal.

Industry/Entity Type

Store

Requirements
Must have
• Your work should meet attached requirements.
Site is multilingual. Wording should assume varieties in length on different languages.
Clean and easy to read UI
Flat design preferrably
Should be based on assets which are free or available for royalty-free licensing
Should not have
• heavy, meaningless 3D and shadow effects
Show NOT copy sites like: plonkra.com, tarnwick.co.uk

```html
<!DOCTYPE html>
<html lang="en">
<head>
<meta charset="utf-8">
<title>velmorino – greeting cards</title>
<link href="https://fonts.googleapis.com/css2?family=Roboto:ital,wght@0,300;0,400;0,500;0,700;1,300;1,700&display=swap" rel="stylesheet">
<style>
:root{
  --page:#ececec;
  --panel:#ffffff;
  --line:#d9d9d9;
  --text:#9a9a9a;
  --text-dark:#555555;
  --teal:#1e8a8a;
  --red:#d9675f;
  --dark-red:#8b1a12;
  --icon-box:#dedede;
  --footer:#d6d6d6;
}
*{box-sizing:border-box;margin:0;padding:0}
html,body{width:1200px;height:2515px;overflow:hidden}
body{background:var(--page);font-family:"Roboto",Arial,sans-serif;color:var(--text);position:relative}
.abs{position:absolute}

/* header */
.brand{left:178px;top:60px;display:flex;align-items:center;gap:10px}
.brand-mark{width:22px;height:22px;background:var(--red)}
.brand-name{font-size:30px;font-weight:400;color:#5b4a44}
.tagline{left:381px;top:20px;font-size:18px;font-weight:700;font-style:italic;color:var(--teal)}
.media-box{top:63px;height:72px;background:var(--icon-box);border-radius:10px;display:flex;align-items:center;justify-content:center;gap:6px}
.media-box span{background:#f4f4f4;border-radius:4px}
.quick{top:72px;text-align:center;font-size:13px;color:#b9b9b9}
.quick svg{display:block;margin:0 auto 4px}
.nav{left:127px;top:149px;width:944px;height:46px;background:var(--panel);border:2px solid var(--line);border-radius:4px}
.nav a{position:absolute;top:0;height:42px;line-height:40px;font-size:15px;color:#aaa;text-decoration:none}
.nav a.active{background:var(--red);color:#fff;padding:0 12px;top:0;height:44px}
.nav a .caret{position:absolute;left:50%;top:25px;width:6px;height:6px;border-right:1px solid #bbb;border-bottom:1px solid #bbb;transform:translateX(-50%) rotate(45deg)}

/* hero */
.hero{left:0;top:206px;width:1200px;height:488px;background:linear-gradient(120deg,#c9b49a 0%,#e4d6bf 35%,#d8c7ad 60%,#9c9088 100%)}
.hero-caption{left:127px;top:528px;width:703px;height:75px;background:rgba(90,70,50,.55);color:#fff;font-size:44px;font-weight:300;font-style:italic;padding:6px 12px}
.hero-arrow{top:440px}
.hero-dots{left:607px;top:658px;display:flex;gap:9px;align-items:center}
.hero-dots i{width:5px;height:5px;border-radius:50%;background:#fff;opacity:.8}
.hero-dots i.on{width:10px;height:10px;background:#f0e0d0}

/* swatches */
.swatches{left:127px;top:705px;width:944px;height:43px;display:flex;gap:3px}
.swatches span{flex:1}
.search{left:127px;top:761px;width:944px;height:45px;background:var(--panel);border:2px solid var(--line);border-radius:4px;display:flex;align-items:center;padding-left:14px;gap:10px;font-size:16px;color:#c7c7c7}

/* categories */
.tags{left:127px;width:944px;display:flex;justify-content:center;gap:7px}
.tag{height:50px;padding:0 14px;line-height:44px;border:3px solid;border-radius:5px;background:#fff;font-size:16px;letter-spacing:.5px}

/* product grid */
.grid{left:127px;top:946px;width:944px;display:flex;gap:19px;align-items:flex-start}
.col{width:222px;display:flex;flex-direction:column;gap:20px}
.card{background:var(--panel);border:2px solid #e2e2e2;border-radius:3px}
.card-img{background:linear-gradient(180deg,#3d6a2c 0%,#c6c8b8 35%,#e0e0d6 60%,#7c7f8e 90%,#4a4f78 100%)}
.card-tags{padding:10px 8px 0;display:flex;flex-wrap:wrap;gap:5px}
.card-tags span{background:#eeeeee;font-size:12px;color:#8f8f8f;padding:2px 8px;border-radius:2px}
.price{text-align:right;font-size:26px;color:#a8a8a8;padding:8px 10px 4px}
.card-foot{border-top:1px solid #ececec;height:36px;display:flex;align-items:center;padding:0 8px;gap:4px}
.card-foot .dot{width:15px;height:15px;border-radius:50%;background:#aaa;margin-left:auto}
.follow{font-size:9px;background:#b5b5b5;color:#fff;border-radius:8px;padding:2px 6px}
.card-foot .cart{margin-left:12px}

/* pagination */
.pager-label{top:2268px;font-size:9px;font-weight:500;color:#aaa;letter-spacing:.5px}
.pager{left:417px;top:2254px;width:363px;height:40px;background:#dcdcdc;border-radius:6px;display:flex;align-items:center;justify-content:space-between;padding:0 8px;font-size:10px;color:#999}
.pager .p{width:26px;height:26px;line-height:26px;text-align:center}
.pager .p.on{background:#eeeeee;border-radius:4px;color:#777}
.pager .p.last{background:#c6c6c6;color:#fff;border-radius:4px}

/* footer */
.footer{left:0;top:2324px;width:1200px;height:191px;background:var(--footer);border-top:3px solid #cfcfcf}
.footer-links{left:365px;top:2360px;list-style:none;font-size:14px;line-height:18px;color:#fff}
.copy{left:129px;top:2430px;font-size:13px;color:#fff}
.newsletter{left:802px;top:2345px;width:266px;height:101px;background:#c5c5c5;border-radius:6px;padding:8px 14px;border:2px solid #bdbdbd}
.newsletter h4{font-size:11px;font-weight:500;color:#fff;letter-spacing:.5px}
.newsletter .field{margin-top:10px;height:30px;background:#eeeeee;border-radius:3px;display:flex;align-items:center;gap:10px;padding-left:10px;font-size:11px;color:#888}
.newsletter .btn{position:absolute;right:22px;bottom:12px;background:var(--teal);color:#fff;font-size:10px;font-weight:500;padding:3px 6px}
</style>
</head>
<body>

<header>
  <div class="abs brand"><span class="brand-mark"></span><span class="brand-name">velmorino</span></div>
  <p class="abs tagline">The individual greeting cards according to your mood</p>

  <div class="abs media-box" style="left:381px;width:113px"><span style="width:40px;height:50px"></span><span style="width:50px;height:38px"></span></div>
  <div class="abs media-box" style="left:542px;width:113px"><span style="width:42px;height:42px"></span></div>
  <div class="abs media-box" style="left:703px;width:113px"><span style="width:40px;height:50px"></span><span style="width:52px;height:38px"></span></div>

  <div class="abs quick" style="left:838px;width:90px">
    <svg width="38" height="34" viewBox="0 0 38 34"><path d="M3 16 L19 3 L35 16 V32 H3 Z" fill="none" stroke="#c4c4c4" stroke-width="3"/></svg>Favorites (0)
  </div>
  <div class="abs quick" style="left:958px;width:60px">
    <svg width="40" height="34" viewBox="0 0 40 34"><path d="M2 4 H9 L14 22 H33 L37 9 H11" fill="none" stroke="#c4c4c4" stroke-width="3"/><circle cx="16" cy="29" r="3" fill="#c4c4c4"/><circle cx="31" cy="29" r="3" fill="#c4c4c4"/></svg>Cart (0)
  </div>

  <nav class="abs nav">
    <a class="active" style="left:58px">All Medias</a>
    <a style="left:249px">Greeting Cards<i class="caret"></i></a>
    <a style="left:415px">Square Cards<i class="caret"></i></a>
    <a style="left:592px">Postcards<i class="caret"></i></a>
    <a style="left:732px">Login<i class="caret"></i></a>
    <a style="left:826px">Contacts<i class="caret"></i></a>
  </nav>
</header>

<section>
  <div class="abs hero" role="img" aria-label="Photo of festive greeting cards with winter illustrations on a table"></div>
  <svg class="abs hero-arrow" style="left:50px" width="20" height="30" viewBox="0 0 20 30"><path d="M15 3 L4 15 L15 27" fill="none" stroke="#fff" stroke-width="5"/></svg>
  <svg class="abs hero-arrow" style="left:1132px" width="20" height="30" viewBox="0 0 20 30"><path d="M5 3 L16 15 L5 27" fill="none" stroke="#fff" stroke-width="5"/></svg>
  <div class="abs hero-caption">Greeting cards for every occasion</div>
  <div class="abs hero-dots"><i></i><i></i><i></i><i class="on"></i><i></i></div>
</section>

<section>
  <div class="abs swatches">
    <span style="background:#8b1a12"></span><span style="background:#e8d9b0"></span><span style="background:#c8c8c8"></span><span style="background:#8e8e8e"></span><span style="background:#f4a6c4"></span><span style="background:#a9bde0"></span><span style="background:#9a5a2a"></span><span style="background:#6fcf3a"></span><span style="background:#3d3d52"></span><span style="background:#2e6a10"></span><span style="background:#d23a3a"></span><span style="background:#6ad3cf"></span><span style="background:#cf6a30"></span><span style="background:#ff9a00"></span><span style="background:#0f6ad6"></span><span style="background:#ffcc2a"></span><span style="background:#e04a8a"></span><span style="background:#2e2ea0"></span><span style="background:#0aa6d8"></span><span style="background:#5e9a10"></span>
  </div>
  <div class="abs search">
    <svg width="30" height="30" viewBox="0 0 30 30"><circle cx="12" cy="12" r="9" fill="none" stroke="#ccc" stroke-width="2.5"/><path d="M12 7 V17 M7 12 H17" stroke="#ccc" stroke-width="2"/><path d="M19 19 L27 27" stroke="#ccc" stroke-width="3"/></svg>
    Search Result for
  </div>

  <div class="abs tags" style="top:821px">
    <span class="tag" style="border-color:var(--dark-red);color:var(--dark-red);font-weight:500">ALL</span>
    <span class="tag" style="border-color:#b8c2d2;color:#a8b4c6">BEARS</span>
    <span class="tag" style="border-color:#a8dede;color:#9fd6d6">BIRTHDAYS</span>
    <span class="tag" style="border-color:#c4c4cc;color:#b4b4bc">CARDS</span>
    <span class="tag" style="border-color:#f2c2c2;color:#eeb0b0">CATS</span>
    <span class="tag" style="border-color:#c8def0;color:#bcd6ec">CONGRATULATIONS</span>
    <span class="tag" style="border-color:#a8d6d6;color:#96cccc">DOGS</span>
    <span class="tag" style="border-color:#b6bac6;color:#a6aab8">FLOWERS</span>
  </div>
  <div class="abs tags" style="top:879px">
    <span class="tag" style="border-color:#eab4ae;color:#e29a92">FOR CHILDREN</span>
    <span class="tag" style="border-color:#b8c2d2;color:#a8b4c6">FRIENDSHIP</span>
    <span class="tag" style="border-color:#a8dede;color:#9fd6d6">LOVE</span>
    <span class="tag" style="border-color:#c4c4cc;color:#b4b4bc">NEWBORN</span>
    <span class="tag" style="border-color:#f2c2c2;color:#eeb0b0">PHOTOS</span>
    <span class="tag" style="border-color:#b8cce6;color:#a8bede">RELIGON</span>
    <span class="tag" style="border-color:#a8dede;color:#9fd6d6">VALENTIN'S DAY</span>
  </div>
</section>

<main class="abs grid">
  <div class="col">
    <article class="card"><div class="card-img" style="height:276px" role="img" aria-label="Christmas card photographed under a decorated tree"></div><div class="card-tags"><span>Fold Studio Design</span><span>Ausra</span><span>Žvaigždes</span><span>Kaledos</span><span>Naujieji metai</span></div><p class="price">€0.00</p><div class="card-foot"><svg width="40" height="18" viewBox="0 0 40 18"><path d="M2 8 L9 2 L16 8 V17 H2 Z M22 8 L29 2 L36 8 V17 H22 Z" fill="none" stroke="#b0b0b0" stroke-width="1.6"/></svg><i class="dot"></i><span class="follow">Follow Us</span><svg class="cart" width="20" height="18" viewBox="0 0 20 18"><path d="M1 2 H4 L7 12 H16 L18 5 H5" fill="none" stroke="#aaa" stroke-width="1.6"/><circle cx="8" cy="15.5" r="1.6" fill="#aaa"/><circle cx="15" cy="15.5" r="1.6" fill="#aaa"/></svg></div></article>
    <article class="card"><div class="card-img" style="height:178px" role="img" aria-label="Christmas card photographed under a decorated tree"></div><div class="card-tags"><span>Fold Studio Design</span><span>Ausra</span><span>Žvaigždes</span><span>Kaledos</span><span>Naujieji metai</span></div><p class="price">€0.00</p><div class="card-foot"><svg width="40" height="18" viewBox="0 0 40 18"><path d="M2 8 L9 2 L16 8 V17 H2 Z M22 8 L29 2 L36 8 V17 H22 Z" fill="none" stroke="#b0b0b0" stroke-width="1.6"/></svg><i class="dot"></i><span class="follow">Follow Us</span><svg class="cart" width="20" height="18" viewBox="0 0 20 18"><path d="M1 2 H4 L7 12 H16 L18 5 H5" fill="none" stroke="#aaa" stroke-width="1.6"/><circle cx="8" cy="15.5" r="1.6" fill="#aaa"/><circle cx="15" cy="15.5" r="1.6" fill="#aaa"/></svg></div></article>
    <article class="card"><div class="card-img" style="height:247px" role="img" aria-label="Christmas card photographed under a decorated tree"></div><div class="card-tags"><span>Fold Studio Design</span><span>Ausra</span><span>Žvaigždes</span><span>Kaledos</span><span>Naujieji metai</span></div><p class="price">€0.00</p><div class="card-foot"><svg width="40" height="18" viewBox="0 0 40 18"><path d="M2 8 L9 2 L16 8 V17 H2 Z M22 8 L29 2 L36 8 V17 H22 Z" fill="none" stroke="#b0b0b0" stroke-width="1.6"/></svg><i class="dot"></i><span class="follow">Follow Us</span><svg class="cart" width="20" height="18" viewBox="0 0 20 18"><path d="M1 2 H4 L7 12 H16 L18 5 H5" fill="none" stroke="#aaa" stroke-width="1.6"/><circle cx="8" cy="15.5" r="1.6" fill="#aaa"/><circle cx="15" cy="15.5" r="1.6" fill="#aaa"/></svg></div></article>
  </div>
  <div class="col" style="margin-top:24px">
    <article class="card"><div class="card-img" style="height:156px" role="img" aria-label="Christmas card photographed under a decorated tree"></div><div class="card-tags"><span>Fold Studio Design</span><span>Ausra</span><span>Žvaigždes</span><span>Kaledos</span><span>Naujieji metai</span></div><p class="price">€0.00</p><div class="card-foot"><svg width="40" height="18" viewBox="0 0 40 18"><path d="M2 8 L9 2 L16 8 V17 H2 Z M22 8 L29 2 L36 8 V17 H22 Z" fill="none" stroke="#b0b0b0" stroke-width="1.6"/></svg><i class="dot"></i><span class="follow">Follow Us</span><svg class="cart" width="20" height="18" viewBox="0 0 20 18"><path d="M1 2 H4 L7 12 H16 L18 5 H5" fill="none" stroke="#aaa" stroke-width="1.6"/><circle cx="8" cy="15.5" r="1.6" fill="#aaa"/><circle cx="15" cy="15.5" r="1.6" fill="#aaa"/></svg></div></article>
    <article class="card"><div class="card-img" style="height:249px" role="img" aria-label="Christmas card photographed under a decorated tree"></div><div class="card-tags"><span>Fold Studio Design</span><span>Ausra</span><span>Žvaigždes</span><span>Kaledos</span><span>Naujieji metai</span></div><p class="price">€0.00</p><div class="card-foot"><svg width="40" height="18" viewBox="0 0 40 18"><path d="M2 8 L9 2 L16 8 V17 H2 Z M22 8 L29 2 L36 8 V17 H22 Z" fill="none" stroke="#b0b0b0" stroke-width="1.6"/></svg><i class="dot"></i><span class="follow">Follow Us</span><svg class="cart" width="20" height="18" viewBox="0 0 20 18"><path d="M1 2 H4 L7 12 H16 L18 5 H5" fill="none" stroke="#aaa" stroke-width="1.6"/><circle cx="8" cy="15.5" r="1.6" fill="#aaa"/><circle cx="15" cy="15.5" r="1.6" fill="#aaa"/></svg></div></article>
    <article class="card"><div class="card-img" style="height:273px" role="img" aria-label="Christmas card photographed under a decorated tree"></div><div class="card-tags"><span>Fold Studio Design</span><span>Ausra</span><span>Žvaigždes</span><span>Kaledos</span><span>Naujieji metai</span></div><p class="price">€0.00</p><div class="card-foot"><svg width="40" height="18" viewBox="0 0 40 18"><path d="M2 8 L9 2 L16 8 V17 H2 Z M22 8 L29 2 L36 8 V17 H22 Z" fill="none" stroke="#b0b0b0" stroke-width="1.6"/></svg><i class="dot"></i><span class="follow">Follow Us</span><svg class="cart" width="20" height="18" viewBox="0 0 20 18"><path d="M1 2 H4 L7 12 H16 L18 5 H5" fill="none" stroke="#aaa" stroke-width="1.6"/><circle cx="8" cy="15.5" r="1.6" fill="#aaa"/><circle cx="15" cy="15.5" r="1.6" fill="#aaa"/></svg></div></article>
  </div>
  <div class="col">
    <article class="card"><div class="card-img" style="height:216px" role="img" aria-label="Christmas card photographed under a decorated tree"></div><div class="card-tags"><span>Fold Studio Design</span><span>Ausra</span><span>Žvaigždes</span><span>Kaledos</span><span>Naujieji metai</span></div><p class="price">€0.00</p><div class="card-foot"><svg width="40" height="18" viewBox="0 0 40 18"><path d="M2 8 L9 2 L16 8 V17 H2 Z M22 8 L29 2 L36 8 V17 H22 Z" fill="none" stroke="#b0b0b0" stroke-width="1.6"/></svg><i class="dot"></i><span class="follow">Follow Us</span><svg class="cart" width="20" height="18" viewBox="0 0 20 18"><path d="M1 2 H4 L7 12 H16 L18 5 H5" fill="none" stroke="#aaa" stroke-width="1.6"/><circle cx="8" cy="15.5" r="1.6" fill="#aaa"/><circle cx="15" cy="15.5" r="1.6" fill="#aaa"/></svg></div></article>
    <article class="card"><div class="card-img" style="height:274px" role="img" aria-label="Christmas card photographed under a decorated tree"></div><div class="card-tags"><span>Fold Studio Design</span><span>Ausra</span><span>Žvaigždes</span><span>Kaledos</span><span>Naujieji metai</span></div><p class="price">€0.00</p><div class="card-foot"><svg width="40" height="18" viewBox="0 0 40 18"><path d="M2 8 L9 2 L16 8 V17 H2 Z M22 8 L29 2 L36 8 V17 H22 Z" fill="none" stroke="#b0b0b0" stroke-width="1.6"/></svg><i class="dot"></i><span class="follow">Follow Us</span><svg class="cart" width="20" height="18" viewBox="0 0 20 18"><path d="M1 2 H4 L7 12 H16 L18 5 H5" fill="none" stroke="#aaa" stroke-width="1.6"/><circle cx="8" cy="15.5" r="1.6" fill="#aaa"/><circle cx="15" cy="15.5" r="1.6" fill="#aaa"/></svg></div></article>
    <article class="card"><div class="card-img" style="height:171px" role="img" aria-label="Christmas card photographed under a decorated tree"></div><div class="card-tags"><span>Fold Studio Design</span><span>Ausra</span><span>Žvaigždes</span><span>Kaledos</span><span>Naujieji metai</span></div><p class="price">€0.00</p><div class="card-foot"><svg width="40" height="18" viewBox="0 0 40 18"><path d="M2 8 L9 2 L16 8 V17 H2 Z M22 8 L29 2 L36 8 V17 H22 Z" fill="none" stroke="#b0b0b0" stroke-width="1.6"/></svg><i class="dot"></i><span class="follow">Follow Us</span><svg class="cart" width="20" height="18" viewBox="0 0 20 18"><path d="M1 2 H4 L7 12 H16 L18 5 H5" fill="none" stroke="#aaa" stroke-width="1.6"/><circle cx="8" cy="15.5" r="1.6" fill="#aaa"/><circle cx="15" cy="15.5" r="1.6" fill="#aaa"/></svg></div></article>
  </div>
  <div class="col">
    <article class="card"><div class="card-img" style="height:249px" role="img" aria-label="Christmas card photographed under a decorated tree"></div><div class="card-tags"><span>Fold Studio Design</span><span>Ausra</span><span>Žvaigždes</span><span>Kaledos</span><span>Naujieji metai</span></div><p class="price">€0.00</p><div class="card-foot"><svg width="40" height="18" viewBox="0 0 40 18"><path d="M2 8 L9 2 L16 8 V17 H2 Z M22 8 L29 2 L36 8 V17 H22 Z" fill="none" stroke="#b0b0b0" stroke-width="1.6"/></svg><i class="dot"></i><span class="follow">Follow Us</span><svg class="cart" width="20" height="18" viewBox="0 0 20 18"><path d="M1 2 H4 L7 12 H16 L18 5 H5" fill="none" stroke="#aaa" stroke-width="1.6"/><circle cx="8" cy="15.5" r="1.6" fill="#aaa"/><circle cx="15" cy="15.5" r="1.6" fill="#aaa"/></svg></div></article>
    <article class="card"><div class="card-img" style="height:214px" role="img" aria-label="Christmas card photographed under a decorated tree"></div><div class="card-tags"><span>Fold Studio Design</span><span>Ausra</span><span>Žvaigždes</span><span>Kaledos</span><span>Naujieji metai</span></div><p class="price">€0.00</p><div class="card-foot"><svg width="40" height="18" viewBox="0 0 40 18"><path d="M2 8 L9 2 L16 8 V17 H2 Z M22 8 L29 2 L36 8 V17 H22 Z" fill="none" stroke="#b0b0b0" stroke-width="1.6"/></svg><i class="dot"></i><span class="follow">Follow Us</span><svg class="cart" width="20" height="18" viewBox="0 0 20 18"><path d="M1 2 H4 L7 12 H16 L18 5 H5" fill="none" stroke="#aaa" stroke-width="1.6"/><circle cx="8" cy="15.5" r="1.6" fill="#aaa"/><circle cx="15" cy="15.5" r="1.6" fill="#aaa"/></svg></div></article>
    <article class="card"><div class="card-img" style="height:214px" role="img" aria-label="Christmas card photographed under a decorated tree"></div><div class="card-tags"><span>Fold Studio Design</span><span>Ausra</span><span>Žvaigždes</span><span>Kaledos</span><span>Naujieji metai</span></div><p class="price">€0.00</p><div class="card-foot"><svg width="40" height="18" viewBox="0 0 40 18"><path d="M2 8 L9 2 L16 8 V17 H2 Z M22 8 L29 2 L36 8 V17 H22 Z" fill="none" stroke="#b0b0b0" stroke-width="1.6"/></svg><i class="dot"></i><span class="follow">Follow Us</span><svg class="cart" width="20" height="18" viewBox="0 0 20 18"><path d="M1 2 H4 L7 12 H16 L18 5 H5" fill="none" stroke="#aaa" stroke-width="1.6"/><circle cx="8" cy="15.5" r="1.6" fill="#aaa"/><circle cx="15" cy="15.5" r="1.6" fill="#aaa"/></svg></div></article>
  </div>
</main>

<nav>
  <span class="abs pager-label" style="left:314px">PREVIOUS PAGE</span>
  <div class="abs pager">
    <svg width="10" height="12" viewBox="0 0 10 12"><path d="M7 1 L2 6 L7 11" fill="none" stroke="#888" stroke-width="2"/></svg>
    <span class="p on">1</span><span class="p">2</span><span class="p">3</span><span class="p">4</span><span class="p">5</span><span class="p">6-14</span><span class="p last">15</span>
  </div>
  <span class="abs pager-label" style="left:797px">NEXT PAGE</span>
</nav>

<footer>
  <div class="abs footer"></div>
  <ul class="abs footer-links">
    <li>About us</li><li>How it works</li><li>Prices</li><li>Rules</li><li>Contacts</li>
  </ul>
  <p class="abs copy">© 2014 velmorino</p>
  <div class="abs newsletter">
    <h4>JOIN THE NEWSLETTER</h4>
    <div class="field">
      <svg width="14" height="11" viewBox="0 0 14 11"><rect x="1" y="1" width="12" height="9" fill="none" stroke="#777" stroke-width="1.2"/><path d="M1 1 L7 6 L13 1" fill="none" stroke="#777" stroke-width="1.2"/></svg>
      yourname@email.com
    </div>
    <span class="btn">SUBSCRIBE</span>
  </div>
</footer>

</body>
</html>
```